Corvane Summit

Need very crisp business cards for Corvane Summit per the logo attached. The vision of Corvane Summit is 'Guide every Venture to Corvane'. I am going into Freelance | Consulting | Contracting and need this communicated on the card. I need the card to provide a clear message of professionalism and what the vision emulates. Will need an area for my website, LinkedIn, Twitter, as fell as the obvious Name, Address, phone, email... on the back, I would like the Vision but receptive to your design ideas.

```html
<!DOCTYPE html>
<html lang="en">
<head>
<meta charset="utf-8">
<title>Corvane Summit — Business Card</title>
<link href="https://fonts.googleapis.com/css2?family=Montserrat:wght@400;500;600&display=swap" rel="stylesheet">
<style>
  :root {
    --navy: #213a70;
    --ink: #2b2b2b;
    --paper: #ffffff;
    --mist: #c9d3ea;
    --backdrop: #1c1c1e;
  }
  * { box-sizing: border-box; margin: 0; padding: 0; }
  html, body {
    width: 1200px; height: 900px; overflow: hidden;
    background: var(--backdrop);
    font-family: "Montserrat", Arial, sans-serif;
  }
  .canvas {
    width: 1200px; height: 900px;
    display: flex; flex-direction: column; align-items: center;
    justify-content: center; gap: 24px;
  }
  .card {
    position: relative;
    width: 680px; height: 389px;
    overflow: hidden;
  }
  /* Front side */
  .card--front {
    background: var(--navy);
    display: flex; flex-direction: column; align-items: center; justify-content: center; gap: 18px;
  }
  .front-lockup { display: flex; align-items: center; gap: 22px; }
  .front-mark {
    width: 34px; height: 34px; border: 6px solid var(--paper);
  }
  .front-name {
    color: var(--paper); font-weight: 600; font-size: 52px; letter-spacing: 0.5px; line-height: 1;
  }
  .front-services {
    color: var(--mist); font-weight: 500; font-size: 15px; letter-spacing: 3px; text-transform: uppercase;
  }
  /* Back side */
  .card--back { background: var(--paper); }
  .brand {
    position: absolute; left: 36px; top: 158px; width: 270px;
  }
  .brand-row { display: flex; align-items: center; gap: 10px; }
  .brand-mark { width: 20px; height: 20px; background: var(--navy); flex: none; }
  .brand-name { color: var(--navy); font-weight: 600; font-size: 26px; line-height: 1; white-space: nowrap; }
  .brand-vision {
    margin-top: 7px; padding-left: 30px;
    color: var(--ink); font-size: 8.5px; font-weight: 500;
    letter-spacing: 1.4px; text-transform: uppercase; white-space: nowrap;
  }
  .divider {
    position: absolute; left: 326px; top: 112px;
    width: 2px; height: 170px; background: var(--navy);
  }
  .contact {
    position: absolute; left: 346px; top: 110px; color: var(--ink);
  }
  .person-name {
    color: var(--navy); font-weight: 500; font-size: 24px; letter-spacing: 0.5px; line-height: 1;
  }
  .person-role { font-size: 16px; margin-top: 3px; margin-bottom: 8px; }
  .contact-line {
    display: flex; align-items: center; gap: 10px;
    font-size: 17px; line-height: 25px;
  }
  .contact-line svg { width: 16px; height: 16px; flex: none; }
  .address { font-size: 17px; line-height: 19px; margin-top: 6px; }
  .band {
    position: absolute; left: 0; right: 0; top: 298px; height: 54px;
    background: var(--navy);
    display: flex; align-items: center; justify-content: center; gap: 14px;
  }
  .social-dot {
    width: 26px; height: 26px; border-radius: 50%; background: var(--paper);
  }
</style>
</head>
<body>
<main class="canvas">
  <section class="card card--front" aria-label="Card front">
    <div class="front-lockup">
      <span class="front-mark"></span>
      <span class="front-name">Corvane Summit</span>
    </div>
    <p class="front-services">Freelance | Consulting | Contracting</p>
  </section>

  <section class="card card--back" aria-label="Card back">
    <div class="brand">
      <div class="brand-row">
        <span class="brand-mark"></span>
        <span class="brand-name">Corvane Summit</span>
      </div>
      <p class="brand-vision">Guide every Venture to Corvane</p>
    </div>
    <div class="divider"></div>
    <div class="contact">
      <p class="person-name">DARA WELLFORD</p>
      <p class="person-role">Sales Manager</p>
      <p class="contact-line">
        <svg viewBox="0 0 16 16" fill="none" stroke="#213a70" stroke-width="1.4"><circle cx="8" cy="8" r="7"/><path d="M5.5 4.5l1.5 1.5-1 1.2a6 6 0 0 0 2.8 2.8l1.2-1 1.5 1.5-1 1a5 5 0 0 1-6-6z"/></svg>
        555-010-2736
      </p>
      <p class="contact-line">
        <svg viewBox="0 0 16 16" fill="none" stroke="#213a70" stroke-width="1.4"><rect x="1" y="3" width="14" height="10"/><path d="M1 3l7 6 7-6"/></svg>
        info@corvanesummit.com
      </p>
      <p class="contact-line">
        <svg viewBox="0 0 16 16" fill="none" stroke="#213a70" stroke-width="1.4"><circle cx="8" cy="8" r="7"/><ellipse cx="8" cy="8" rx="3" ry="7"/><path d="M1 8h14M2.5 4.5h11M2.5 11.5h11"/></svg>
        www.corvanesummit.com
      </p>
      <p class="address">PO Box 208, Larkfield<br>Qld 4702</p>
    </div>
    <div class="band">
      <span class="social-dot"></span>
      <span class="social-dot"></span>
    </div>
  </section>
</main>
</body>
</html>
```